Web design for a honey company

We are a honey retailing company currently looking for creative design for 3 pages of our existing e-commerce website which can be found here www.alpha.kestrowfarms.co.nz. The designs need to be responsive i.e. presented in both desktop and mobile versions. We want to use the existing page color pallet, however any fonts can be used. Please use the texts and graphic content in the attachment files provided. For more detailed instructions please. The page does not require coding, the output files should be provided as layered and editable PSD.<br/><br/>Task 2: design 2 home page banners. Images, texts and the concept provided in the "layout structure" file. <br/><br/>The web designs should be presented in both desktop and mobile versions. We are looking for professional designer submissions only!

Target Market(s)

Hi-end consumers
Health conscious consumers

Number of Pages Required

3 page

Requirements
Must have
• 50% of images supplied along + any suggested stock images.
• Supplied texts integrated in the designs.
• Please only use the product images we have provided!
Should not have
• Clipart vector bees, vector honey slots or combs.
• No images of honey in glass jars!
• Do not use images of the traditional honey wooden spoons!
• Do not use images of any other but Manuka flower!

```html
<!DOCTYPE html>
<html lang="en">
<head>
<meta charset="utf-8">
<title>Kestrow Manuka Honey – Home</title>
<link href="https://fonts.googleapis.com/css2?family=Poppins:wght@400;500;600&family=Roboto:wght@400;500&display=swap" rel="stylesheet">
<style>
:root{
  --dark:#2c2f33;
  --footer:#232323;
  --orange:#f5a623;
  --orange-deep:#f26b21;
  --honey:#fdd835;
  --honey-deep:#f7c21a;
  --brown:#5b3a2c;
  --blue:#1565c0;
  --band:rgba(30,110,185,.72);
  --cream:#f7f5f0;
  --ink:#333;
  --muted:#555;
  --white:#fff;
}
*{margin:0;padding:0;box-sizing:border-box}
html,body{width:1200px;height:2884px;overflow:hidden}
body{position:relative;font-family:"Poppins",sans-serif;color:var(--ink);background:var(--cream)}
.abs{position:absolute}
.header{left:0;top:0;width:1200px;height:90px;background:var(--dark)}
.brand{display:flex;align-items:center;gap:8px;color:var(--honey);font-weight:600;font-size:22px;letter-spacing:2px}
.brand .dot{width:14px;height:14px;border-radius:50%;background:var(--honey)}
.header .brand{left:140px;top:31px}
.nav{left:297px;top:36px;font-size:12.5px;font-weight:600;color:var(--white)}
.nav span{position:absolute;white-space:nowrap}
.nav .active{color:var(--orange)}
.login{left:900px;top:36px;color:var(--orange);font-size:13px;font-weight:500}
.cart-count{left:998px;top:27px;width:16px;height:16px;border-radius:50%;background:var(--orange-deep);color:#fff;font-size:10px;text-align:center;line-height:16px}
.dropdown{left:348px;top:90px;width:196px;height:84px;background:rgba(40,44,50,.92);font-family:"Roboto",sans-serif;font-size:11.5px;color:#fff;padding:8px 11px}
.dropdown div{height:25px;line-height:20px;border-bottom:1px solid rgba(255,255,255,.35)}
.dropdown div:last-child{border:0}
.hero{left:0;top:90px;width:1200px;height:582px;background:linear-gradient(180deg,#4c7fb7 0%,#7ea0c2 22%,#8b7a4e 45%,#b28a43 62%,#8d6a47 78%,#7b5a3e 100%)}
.hero-title{left:0;top:236px;width:1200px;text-align:center;color:#fff;font-size:29px;font-weight:600}
.hero-band{left:0;top:431px;width:1200px;height:129px;background:var(--band)}
.hero-copy{left:608px;top:448px;width:480px;color:#fff;font-size:23px;line-height:27px}
.arrow{top:225px;width:24px;height:54px;background:rgba(40,44,50,.75)}
.hero-jars{left:128px;top:332px;width:462px;height:258px;border-radius:10px;background:linear-gradient(180deg,#2a2a2a,#1d3a34 55%,#2a2a2a)}
.drip{left:0;top:600px}
.featured{left:0;top:672px;width:1200px;height:591px;background:var(--honey)}
.h2{width:1200px;left:0;text-align:center;color:var(--brown);font-weight:400;font-size:38px;line-height:38px}
.squiggle{width:32px;height:6px}
.product{width:220px;text-align:center}
.jar{margin:0 auto;width:188px;height:274px;border-radius:14px;background:linear-gradient(180deg,#2b2b2b 0 22%,#1e2e2a 22% 55%,#1d4b3f 75%,#262626)}
.product h3{margin-top:28px;font-weight:400;font-size:22px;color:var(--brown);line-height:24px}
.product p{font-size:14px;color:var(--ink);margin-top:2px}
.btn{display:inline-block;margin-top:13px;width:108px;height:31px;line-height:31px;border-radius:16px;background:var(--blue);color:#fff;font-size:14px;font-weight:500}
.card{top:1458px;width:228px;height:368px;background:#fff;border:1px solid #e6e2d8;text-align:center}
.card .photo{height:142px}
.card h4{font-weight:400;font-size:16.5px;line-height:19px;color:var(--ink);margin:12px 12px 0}
.card .squiggle{margin:4px auto 0;display:block}
.card p{font-family:"Roboto",sans-serif;font-size:10.3px;line-height:14.5px;color:var(--muted);margin:10px 10px 0}
.card a{position:absolute;left:0;width:100%;top:344px;font-size:12px;color:var(--brown);text-decoration:underline}
.video-band{left:0;top:2138px;width:1200px;height:472px;background:var(--honey)}
.video{left:116px;top:1958px;width:967px;height:488px;background:linear-gradient(160deg,#4d5a3e,#7b8a6e 40%,#a8aea0 55%,#5b6648)}
.play{left:556px;top:2157px}
.subscribe-label{left:121px;top:2544px;font-size:16px;color:var(--brown);font-weight:500}
.input{left:364px;top:2539px;width:548px;height:32px;border-radius:16px;background:#fff;font-family:"Roboto",sans-serif;font-size:10px;color:#555;padding:9px 0 0 20px}
.sub-btn{left:825px;top:2539px;width:87px;height:32px;border-radius:16px;background:var(--orange-deep);color:#fff;font-size:12px;text-align:center;line-height:32px}
.follow{left:941px;top:2548px;font-size:11px;color:var(--ink);display:flex;align-items:center;gap:7px}
.follow i{width:9px;height:9px;border-radius:50%;background:var(--orange-deep);display:inline-block}
.footer{left:0;top:2610px;width:1200px;height:274px;background:var(--footer)}
.flinks{font-size:12px;color:#fff;line-height:20px}
.pay{left:0;top:2800px;width:1200px;display:flex;justify-content:center;gap:14px;font-size:13px;font-weight:600;color:#8aa0c8}
.copy{left:0;top:2836px;width:1200px;text-align:center;font-size:11px;color:#fff}
</style>
</head>
<body>

<header class="abs header">
  <div class="abs brand"><span class="dot"></span>KESTROW</div>
  <nav class="abs nav">
    <span style="left:0">Home</span>
    <span class="active" style="left:53px">Shop ⌄</span>
    <span style="left:112px">MGO Manuka honey ⌄</span>
    <span style="left:265px">About Us ⌄</span>
    <span style="left:353px">Contact Us ⌄</span>
  </nav>
  <div class="abs login">Login</div>
  <svg class="abs" style="left:956px;top:34px" width="22" height="20" viewBox="0 0 22 20"><path d="M11 18 C-4 8 4 -3 11 5 C18 -3 26 8 11 18Z" fill="none" stroke="#fff" stroke-width="2"/></svg>
  <svg class="abs" style="left:988px;top:35px" width="22" height="20" viewBox="0 0 22 20"><path d="M1 2h4l3 11h11l2-8H7" fill="none" stroke="#fff" stroke-width="2"/><circle cx="9" cy="17" r="1.8" fill="#fff"/><circle cx="18" cy="17" r="1.8" fill="#fff"/></svg>
  <div class="abs cart-count">0</div>
</header>

<section class="abs hero" role="img" aria-label="Mountain valley landscape with honey jars on a wooden deck"></section>
<div class="abs hero-band"></div>
<div class="abs hero-jars" role="img" aria-label="Three jars of Kestrow Manuka honey"></div>
<h1 class="abs hero-title">The purest Manuka honey from the purest environment</h1>
<p class="abs hero-copy">Just New Zealand's unique plant and native bees working in harmony to make the best honey in the world.</p>
<div class="abs arrow" style="left:0"><svg width="24" height="54"><path d="M15 21l-6 6 6 6" stroke="var(--orange)" stroke-width="2.5" fill="none"/></svg></div>
<div class="abs arrow" style="left:1176px"><svg width="24" height="54"><path d="M9 21l6 6-6 6" stroke="var(--orange)" stroke-width="2.5" fill="none"/></svg></div>
<div class="abs dropdown">
  <div>MGO science (what is MGO)</div>
  <div>MGO vs KGF</div>
  <div>Quality, MGO certification</div>
</div>
<svg class="abs drip" width="1200" height="74" viewBox="0 0 1200 74"><path d="M0 40 C80 20 140 55 230 38 S380 18 470 40 S620 55 700 36 S860 18 950 38 S1110 55 1200 34 V74 H0Z" fill="var(--honey)"/></svg>

<section class="abs featured"></section>
<h2 class="abs h2" style="top:716px">Featured Products</h2>
<svg class="abs squiggle" style="left:584px;top:764px" viewBox="0 0 32 6"><path d="M0 3 Q4 0 8 3 T16 3 T24 3 T32 3" stroke="var(--orange-deep)" stroke-width="2" fill="none"/></svg>

<div class="abs product" style="left:161px;top:828px"><div class="jar" role="img" aria-label="Manuka honey MGO 400 jar"></div><h3>Manuka Honey</h3><p>MGO 400</p><span class="btn">Buy Now</span></div>
<div class="abs product" style="left:490px;top:828px"><div class="jar" role="img" aria-label="Manuka honey MGO 500 jar"></div><h3>Manuka Honey</h3><p>MGO 500</p><span class="btn">Buy Now</span></div>
<div class="abs product" style="left:818px;top:828px"><div class="jar" role="img" aria-label="Manuka honey MGO 800 jar"></div><h3>Manuka Honey</h3><p>MGO 800</p><span class="btn">Buy Now</span></div>

<h2 class="abs h2" style="top:1316px">Our Manuka honey –<br>unlike anything in the world.</h2>
<svg class="abs squiggle" style="left:584px;top:1413px" viewBox="0 0 32 6"><path d="M0 3 Q4 0 8 3 T16 3 T24 3 T32 3" stroke="var(--orange-deep)" stroke-width="2" fill="none"/></svg>
<div class="abs" style="left:1007px;top:1293px;width:193px;height:190px;background:radial-gradient(ellipse at 55% 45%,#3a8ed8 0%,#5bb0e6 40%,rgba(247,245,240,0) 70%)" role="img" aria-label="Low-poly kingfisher perched on a branch"></div>

<article class="abs card" style="left:116px">
  <div class="photo" style="background:linear-gradient(180deg,#8fb4e0,#b7a08f 55%,#3b7fb7 70%,#5f7a3a)" role="img" aria-label="Lake and mountains of New Zealand"></div>
  <h4>KestrowManukaHoney – The purest taste of New Zealand</h4>
  <svg class="squiggle" viewBox="0 0 32 6"><path d="M0 3 Q4 0 8 3 T16 3 T24 3 T32 3" stroke="var(--orange-deep)" stroke-width="2" fill="none"/></svg>
  <p>Tucked away at the edge of the world, New Zealand's natural environment has evolved like no other. Its native plants have been used by the indigenous people of New Zealand for hundreds of years for their healing properties.</p>
  <a>Read more</a>
</article>
<article class="abs card" style="left:364px">
  <div class="photo" style="background:linear-gradient(180deg,#6b7552,#cfc9c4 50%,#55603f)" role="img" aria-label="Manuka flowers in bloom"></div>
  <h4>Only the best will do</h4>
  <svg class="squiggle" viewBox="0 0 32 6"><path d="M0 3 Q4 0 8 3 T16 3 T24 3 T32 3" stroke="var(--orange-deep)" stroke-width="2" fill="none"/></svg>
  <p>As any great chef will tell you, the quality of a dish depends on the quality of your ingredients. For our honey, the first ingredient is the Manukaflower. The locations for our hives are carefully chosen by our beekeepers to make sure that the bees have access to the most abundant areas of Manuka plants...</p>
  <a>Read more</a>
</article>
<article class="abs card" style="left:609px">
  <div class="photo" style="background:linear-gradient(180deg,#7a4a22,#b7793b 50%,#d9a566)" role="img" aria-label="Bees at the entrance of a wooden hive"></div>
  <h4>Protecting our bees</h4>
  <svg class="squiggle" viewBox="0 0 32 6"><path d="M0 3 Q4 0 8 3 T16 3 T24 3 T32 3" stroke="var(--orange-deep)" stroke-width="2" fill="none"/></svg>
  <p>The proprietary processes our beekeepersuse to harvest and extract our Manuka honeyare designed to protect our bees. As far as we're concerned, our bees are part of the team and we treat them with respect. That includes minimising our impact on their natural behaviour and maintaining their natural habitat.</p>
  <a>Read more</a>
</article>
<article class="abs card" style="left:855px">
  <div class="photo" style="background:linear-gradient(135deg,#8a8a80,#9a7040 45%,#c49a55 70%,#5a5a4a)" role="img" aria-label="Hive frame covered with bees"></div>
  <h4>True MGO certified Manuka Honey</h4>
  <svg class="squiggle" viewBox="0 0 32 6"><path d="M0 3 Q4 0 8 3 T16 3 T24 3 T32 3" stroke="var(--orange-deep)" stroke-width="2" fill="none"/></svg>
  <p>And finally comes the science part. Kestrow honey come a long way from the remote locations of New Zealand to your pantry. On its way we make sure every drop of our honey istested by an independent NALC-certified laboratory to verify that it has been made using the nectar from the Manuka flower...</p>
  <a>Read more</a>
</article>
<div class="abs" style="left:0;top:1763px;width:190px;height:134px;background:radial-gradient(ellipse at 40% 50%,#e8a6b8 0%,#f2cdd6 35%,rgba(247,245,240,0) 70%)" role="img" aria-label="Sprig of Manuka blossom"></div>

<div class="abs video-band"></div>
<svg class="abs" style="left:0;top:2128px" width="1200" height="24" viewBox="0 0 1200 24"><path d="M0 12 C40 2 80 18 116 10 V24 H0Z M1083 10 C1120 2 1160 18 1200 8 V24 H1083Z" fill="var(--honey)"/></svg>
<div class="abs video" role="img" aria-label="Video still of a beekeeper in a protective suit tending hives"></div>
<svg class="abs play" width="90" height="90" viewBox="0 0 90 90"><circle cx="45" cy="45" r="45" fill="var(--honey)"/><path d="M36 30v30l25-15z" fill="var(--brown)"/></svg>

<div class="abs subscribe-label">Subscribe for weekly news</div>
<div class="abs input">Your email...</div>
<div class="abs sub-btn">Subscribe</div>
<div class="abs follow">Follow us - <i></i><i></i><i></i><i></i></div>

<footer class="abs footer"></footer>
<div class="abs brand" style="left:168px;top:2678px;font-size:26px"><span class="dot"></span>KESTROW</div>
<div class="abs flinks" style="left:376px;top:2671px">Shop Manuka honey<br>Shop Native honey</div>
<div class="abs flinks" style="left:552px;top:2671px">About us<br>Contacts</div>
<div class="abs flinks" style="left:652px;top:2671px">Terms &amp; Conditions<br>Privacy Policy</div>
<div class="abs flinks" style="left:814px;top:2671px">Returns policy<br>FAQs</div>
<div class="abs flinks" style="left:942px;top:2671px">Partnership enquiries</div>
<div class="abs pay"><span>PayWise</span><span>CardOne</span><span>Vantra</span></div>
<div class="abs copy">© 2020 Kestrow</div>

</body>
</html>
```